Vantor K (digital construction product company)'s trade show booth

Our company is called Vantor K Limited, which is a spin-off from a traditional construction company in Hong Kong called Hollister Construction.

We position ourselves as distinct from traditional construction as digital construction technologies for future.

We are the distributors for a few products from startups which are related to construction. One of the products is this concrete sensor - www.pelmarix.io.

Vantor K's vision statement is "To accelerate the digital revolution in the construction industry & urban environment"

Vantor K is to disrupt traditional construction industry and the ultimate goal is to have a unified digital system for all equipment, process and materials in a construction site. All the companies that we are distributing are part of this journey.

We are going to have a small trade show booth - a table, a screen and some spaces for pull-out banners. Vantor K just started the business operation one year ago, and this is the first time to do a trade booth. We want to take this opportunity to have a design of a theme that will be useful for all future promotion events.

The design should communicate the vision of Vantor K, and very simply present each subsidiary company for a particular digital task of the construction process as a piece of puzzle. The 5 products are shown in the attached 20190816 - Vantor K products
Say, now there are 5 puzzles like this:
1. Concrete strength & quality
2. Site condition & deformation
3. Site surveillance & security
4. Clean energy
5. Site spatial & reality cloud platform

The background of the design (say, the pull-out banner) should be clear, and look like a real-photo. The puzzle should be 3D. I particularly like this design - https://qvt.wxp

The concept of puzzles can also make reference to the attached reference 2.pdf. The faces of the puzzles are the 5 functions mentioned above. But in future, these data can be augmented with 'Insights', and 'Machine-learning to Optimize Processes'. I hope these concepts can also be bought about in the design.

The logo of Vantor K is attached.

I like a plain background color like https://qvt.wxp. But fully white background looks strange for a pull-out banner. If patches of the blue color match the design, you can also consider.

```html
<!DOCTYPE html>
<html lang="en">
<head>
<meta charset="utf-8">
<title>Vantor K – Pull-up Banner</title>
<link href="https://fonts.googleapis.com/css2?family=Oswald:wght@400;500&display=swap" rel="stylesheet">
<style>
  :root{
    --stage:#e3e8ee;
    --sky:#a6cce4;
    --deep-sky:#6a9bbf;
    --paper:#ffffff;
    --brand-blue:#3f8fca;
    --brand-grey:#8a8b8d;
    --concrete:#e84a4a;
    --concrete-text:#e03c3c;
    --orange:#f26b21;
    --amber:#f5b82e;
    --energy:#8dc63f;
    --energy-text:#9bc53d;
    --teal:#2fb5c0;
    --teal-text:#3bb6c8;
    --violet:#6c4c9c;
    --violet-text:#6b4fa0;
    --slate:#6f7fae;
  }
  html,body{margin:0;padding:0;width:706px;height:1200px;overflow:hidden;background:var(--stage);}
  .canvas{position:relative;width:706px;height:1200px;display:flex;align-items:center;justify-content:center;}
  .banner{display:block;width:470px;height:1168px;box-shadow:0 4px 18px rgba(0,0,0,.18);}
  .label{font-family:'Oswald',sans-serif;font-weight:400;font-size:30px;}
  .brand-name{font-family:'Oswald',sans-serif;font-weight:500;font-size:170px;fill:var(--brand-grey);}
</style>
</head>
<body>
<main class="canvas">
  <svg class="banner" viewBox="0 0 867 2155" xmlns="http://www.w3.org/2000/svg" aria-label="Vantor K pull-up banner">
    <defs>
      <linearGradient id="paperFade" x1="0" y1="0" x2="0" y2="1">
        <stop offset="0" stop-color="#ffffff"/>
        <stop offset=".45" stop-color="#f6f9fc"/>
        <stop offset="1" stop-color="#c7d5e0"/>
      </linearGradient>
      <linearGradient id="footFade" x1="0" y1="0" x2="0" y2="1">
        <stop offset="0" stop-color="#86afcd"/>
        <stop offset="1" stop-color="var(--deep-sky)"/>
      </linearGradient>
    </defs>

    <rect class="band-top" width="867" height="400" fill="var(--sky)"/>
    <rect class="band-bottom" y="1800" width="867" height="355" fill="url(#footFade)"/>
    <path class="field" d="M0 160 Q433 0 867 160 L867 1945 Q433 2150 0 1945 Z" fill="url(#paperFade)"/>
    <path class="field-edge" d="M0 1945 Q433 2150 867 1945" fill="none" stroke="#e9eef3" stroke-width="14"/>
    <path class="field-edge" d="M0 160 Q433 0 867 160" fill="none" stroke="#f1f1f1" stroke-width="10"/>

    <rect class="brand-square" x="340" y="150" width="165" height="160" fill="var(--brand-blue)"/>
    <text class="brand-name" x="433" y="505" text-anchor="middle">Vantor K</text>

    <g class="connectors" fill="none" stroke-width="3">
      <path d="M229 985 V1385 Q150 1390 110 1430" stroke="var(--orange)"/>
      <path d="M671 940 V1205 Q671 1217 659 1217 H589" stroke="#a9d9d4"/>
      <path d="M687 937 V1223 Q687 1235 675 1235 H598 Q586 1235 586 1247 V1590" stroke="var(--energy)"/>
      <path d="M470 1337 V1745 Q470 1758 483 1758 H545" stroke="#c1cc35"/>
      <path d="M439 1360 V1652 Q439 1670 421 1670 H222" stroke="#f39a2b"/>
    </g>

    <g class="module module-concrete">
      <circle cx="229" cy="865" r="142" fill="none" stroke="var(--orange)" stroke-width="2" pathLength="100" stroke-dasharray="42 58" transform="rotate(100 229 865)"/>
      <circle cx="229" cy="865" r="142" fill="none" stroke="var(--amber)" stroke-width="2" pathLength="100" stroke-dasharray="28 72" transform="rotate(-100 229 865)"/>
      <circle cx="229" cy="865" r="122" fill="none" stroke="var(--orange)" stroke-width="4" pathLength="100" stroke-dasharray="62 38" transform="rotate(-185 229 865)"/>
      <circle cx="229" cy="865" r="96" fill="var(--paper)" stroke="var(--concrete)" stroke-width="18"/>
      <circle cx="130" cy="963" r="6" fill="var(--orange)"/>
      <rect x="162" y="820" width="133" height="80" fill="#cf2a2a" role="img" aria-label="Illustration of a red 3D building brick"/>
      <text class="label" x="63" y="703" textLength="345" lengthAdjust="spacingAndGlyphs" fill="var(--concrete-text)">CONCRETE STRENGTH &amp; QUALITY</text>
    </g>

    <g class="module module-energy">
      <circle cx="671" cy="807" r="132" fill="none" stroke="#a9d9d4" stroke-width="2" pathLength="100" stroke-dasharray="55 45" transform="rotate(-5 671 807)"/>
      <circle cx="671" cy="807" r="132" fill="none" stroke="var(--slate)" stroke-width="2" pathLength="100" stroke-dasharray="25 75" transform="rotate(-90 671 807)"/>
      <circle cx="671" cy="807" r="110" fill="none" stroke="var(--violet)" stroke-width="4" pathLength="100" stroke-dasharray="40 60" transform="rotate(-150 671 807)"/>
      <circle cx="671" cy="807" r="84" fill="var(--paper)" stroke="var(--energy)" stroke-width="14"/>
      <circle cx="687" cy="937" r="5" fill="var(--energy)"/>
      <rect x="617" y="750" width="112" height="112" fill="#3f7fb8" role="img" aria-label="Illustration of a multicoloured 3D puzzle cube"/>
      <text class="label" x="593" y="662" textLength="154" lengthAdjust="spacingAndGlyphs" fill="var(--energy-text)">CLEAN ENERGY</text>
    </g>

    <g class="module module-surveillance">
      <circle cx="444" cy="1217" r="143" fill="none" stroke="var(--amber)" stroke-width="2" pathLength="100" stroke-dasharray="65 35" transform="rotate(40 444 1217)"/>
      <circle cx="444" cy="1217" r="124" fill="none" stroke="var(--energy)" stroke-width="4" pathLength="100" stroke-dasharray="45 55" transform="rotate(-60 444 1217)"/>
      <circle cx="444" cy="1217" r="124" fill="none" stroke="#f2c32e" stroke-width="4" pathLength="100" stroke-dasharray="22 78" transform="rotate(-175 444 1217)"/>
      <circle cx="444" cy="1217" r="98" fill="var(--paper)" stroke="var(--teal)" stroke-width="16"/>
      <circle cx="331" cy="1262" r="6" fill="var(--teal)"/>
      <rect x="382" y="1155" width="126" height="126" fill="#5b8f55" role="img" aria-label="Illustration of a blue, pink and green 3D cube"/>
      <text class="label" x="277" y="1055" textLength="341" lengthAdjust="spacingAndGlyphs" fill="var(--teal-text)">SITE SURVEILLANCE &amp; SECURITY</text>
    </g>

    <g class="module module-condition">
      <circle cx="229" cy="1513" r="158" fill="none" stroke="var(--orange)" stroke-width="2" pathLength="100" stroke-dasharray="45 55" transform="rotate(60 229 1513)"/>
      <circle cx="229" cy="1513" r="128" fill="none" stroke="var(--orange)" stroke-width="4" pathLength="100" stroke-dasharray="55 45" transform="rotate(90 229 1513)"/>
      <circle cx="229" cy="1513" r="128" fill="none" stroke="var(--amber)" stroke-width="4" pathLength="100" stroke-dasharray="25 75" transform="rotate(0 229 1513)"/>
      <circle cx="229" cy="1513" r="100" fill="var(--paper)" stroke="var(--orange)" stroke-width="18"/>
      <circle cx="355" cy="1514" r="7" fill="var(--orange)"/>
      <rect x="160" y="1467" width="137" height="92" fill="#c7a23e" role="img" aria-label="Illustration of a wall of multicoloured building bricks"/>
      <text class="label" x="48" y="1718" textLength="349" lengthAdjust="spacingAndGlyphs" fill="var(--concrete-text)">SITE CONDITION &amp; DEFORMATION</text>
    </g>

    <g class="module module-spatial">
      <circle cx="662" cy="1713" r="145" fill="none" stroke="var(--slate)" stroke-width="2" pathLength="100" stroke-dasharray="30 70" transform="rotate(-110 662 1713)"/>
      <circle cx="662" cy="1713" r="125" fill="none" stroke="var(--energy)" stroke-width="4" pathLength="100" stroke-dasharray="35 65" transform="rotate(90 662 1713)"/>
      <circle cx="662" cy="1713" r="125" fill="none" stroke="var(--slate)" stroke-width="4" pathLength="100" stroke-dasharray="38 62" transform="rotate(-10 662 1713)"/>
      <circle cx="662" cy="1713" r="98" fill="var(--paper)" stroke="var(--violet)" stroke-width="16"/>
      <circle cx="556" cy="1645" r="6" fill="var(--violet)"/>
      <rect x="604" y="1640" width="116" height="150" fill="#8a5a6e" role="img" aria-label="Illustration of a tall multicoloured 3D puzzle block"/>
      <text class="label" x="376" y="1890" textLength="449" lengthAdjust="spacingAndGlyphs" fill="var(--violet-text)">SITE SPATIAL &amp; REALITY CLOUD PLATFORM</text>
    </g>
  </svg>
</main>
</body>
</html>
```